Stonefield General Contracting Business Card

My company is a General Contracting and Handyman service based in a private community in Northeast Pennsylvania.
Our cliental is a mix of year round and seasonal homeowners
We pride ourselves i using new and innovative building techniques and always try to build with pride and integrity
Please check my website f(under construction) or a list of services and more information
The files below are my logo and my facebook business page profile pic

Industry/Entity Type

Building

Contact Information for Business Card

Stonefield General Contracting
Dale Hurtig
Pine Hollow, Pennsylvania
570-314-2796
dale@stnfldco.com
www.stnfldco.com
www.pagenook.example/stonefieldcontracting

```html
<!DOCTYPE html>
<html lang="en">
<head>
<meta charset="utf-8">
<title>Stonefield General Contracting – Business Card</title>
<link rel="stylesheet" href="https://fonts.googleapis.com/css2?family=Open+Sans:wght@400;600;700&display=swap">
<style>
  :root {
    --backdrop: #111111;
    --card-white: #ececec;
    --wood-light: #c9b49c;
    --wood-mid: #b59e85;
    --ink: #1b1b1b;
    --accent-red: #e0321c;
    --divider: #c8c8c8;
  }
  html, body {
    margin: 0;
    padding: 0;
    width: 1200px;
    height: 1000px;
    overflow: hidden;
    background: var(--backdrop);
    font-family: "Open Sans", Arial, sans-serif;
  }
  .canvas {
    position: relative;
    width: 1200px;
    height: 1000px;
  }
  .card {
    position: absolute;
    left: 261px;
    width: 679px;
    height: 385px;
    border-radius: 24px;
    overflow: hidden;
  }
  .card--front {
    top: 90px;
    background: linear-gradient(160deg, var(--wood-light), var(--wood-mid));
  }
  .card--back {
    top: 525px;
    background: var(--card-white);
  }
  .brand {
    position: absolute;
    display: flex;
    align-items: center;
    gap: 14px;
    color: var(--ink);
    font-weight: 700;
    line-height: 1.05;
    text-transform: uppercase;
  }
  .brand__mark {
    flex: none;
    background: var(--accent-red);
  }
  .brand--front {
    left: 0;
    right: 0;
    top: 156px;
    justify-content: center;
    font-size: 38px;
  }
  .brand--front .brand__mark { width: 66px; height: 66px; }
  .brand--back {
    left: 20px;
    width: 300px;
    top: 160px;
    justify-content: center;
    font-size: 24px;
  }
  .brand--back .brand__mark { width: 42px; height: 42px; }
  .brand__name span { display: block; font-size: 0.52em; letter-spacing: 0.16em; }
  .card__divider {
    position: absolute;
    left: 339px;
    top: 60px;
    width: 2px;
    height: 295px;
    background: linear-gradient(to bottom, transparent, var(--divider) 20%, var(--divider) 80%, transparent);
  }
  .contact {
    position: absolute;
    left: 371px;
    top: 118px;
    color: var(--ink);
  }
  .contact__name {
    margin: 0 0 14px;
    font-size: 28px;
    font-weight: 400;
    line-height: 1.2;
  }
  .contact__name strong { font-weight: 700; }
  .contact__list {
    list-style: none;
    margin: 0;
    padding: 0;
    font-size: 16.5px;
    font-weight: 600;
  }
  .contact__list li {
    display: flex;
    align-items: center;
    gap: 10px;
    height: 22.6px;
  }
  .contact__icon {
    width: 16px;
    height: 16px;
    flex: none;
    fill: var(--accent-red);
  }
</style>
</head>
<body>
<div class="canvas">
  <section class="card card--front" role="img" aria-label="Light oak wood grain card face">
    <div class="brand brand--front">
      <div class="brand__mark"></div>
      <div class="brand__name">Stonefield<span>General Contracting</span></div>
    </div>
  </section>

  <section class="card card--back">
    <div class="brand brand--back">
      <div class="brand__mark"></div>
      <div class="brand__name">Stonefield<span>General Contracting</span></div>
    </div>
    <div class="card__divider"></div>
    <div class="contact">
      <h1 class="contact__name"><strong>Dale</strong> Hurtig</h1>
      <ul class="contact__list">
        <li>
          <svg class="contact__icon" viewBox="0 0 16 16"><path d="M1 6c0-2 3-4 7-4s7 2 7 4v1h-4V5.5H5V7H1zM4 8h8l2 6H2z"/></svg>
          570-314-2796
        </li>
        <li>
          <svg class="contact__icon" viewBox="0 0 16 16"><path d="M1 3h14v10H1z M2.5 4.5 8 9l5.5-4.5" fill="none" stroke="#e0321c" stroke-width="1.6"/></svg>
          dale@stnfldco.com
        </li>
        <li>
          <svg class="contact__icon" viewBox="0 0 16 16"><rect x="1" y="1" width="14" height="14" rx="1.5"/></svg>
          /stonefieldcontracting
        </li>
        <li>
          <svg class="contact__icon" viewBox="0 0 16 16"><g fill="none" stroke="#e0321c" stroke-width="1.5"><circle cx="8" cy="8" r="6.5"/><ellipse cx="8" cy="8" rx="3" ry="6.5"/><path d="M1.5 8h13M2.5 5h11M2.5 11h11"/></g></svg>
          www.stnfldco.com
        </li>
        <li>
          <svg class="contact__icon" viewBox="0 0 16 16"><path d="M8 1a5 5 0 0 1 5 5c0 3.5-5 9-5 9S3 9.5 3 6a5 5 0 0 1 5-5zm0 3a2 2 0 1 0 0 4 2 2 0 0 0 0-4z"/></svg>
          Pine Hollow, Pennsylvania
        </li>
      </ul>
    </div>
  </section>
</div>
</body>
</html>
```